Business Card Design

Please use the Logo for colors and styles, and create a business card using the following info:

Matthias Loeber
Web Developer

Loeber Solutions
+41 76 482 17 05
matthias@loeber-solutions.example
www.loeber-solutions.example

Download the logo at http://loeber-solutions.example/tl_files/loeber_solutions.zip

Thanks for your works!

```html
<!DOCTYPE html>
<html lang="en">
<head>
<meta charset="utf-8">
<title>Loeber Solutions – Business Card</title>
<link rel="stylesheet" href="https://fonts.googleapis.com/css2?family=Arimo:wght@400;500&family=Cormorant+Garamond:wght@500&display=swap">
<style>
  :root {
    --brand-blue: #0b78c2;
    --brand-navy: #0d4670;
    --band-top: #0c4573;
    --band-mid: #136aa6;
    --band-glow: #1b8fd6;
    --floor-top: #0a7cc9;
    --floor-bottom: #0a4d84;
    --paper: #ffffff;
    --label: #173b5b;
    --text-light: #ffffff;
  }
  * { box-sizing: border-box; margin: 0; padding: 0; }
  html, body { width: 1200px; height: 900px; overflow: hidden; background: var(--paper); }
  .board { position: relative; width: 1200px; height: 900px; font-family: "Arimo", Arial, sans-serif; }

  .masthead { position: absolute; inset: 0 0 auto 0; height: 210px; background: var(--paper);
    display: flex; align-items: center; justify-content: center; }
  .wordmark { font-family: "Arimo", Arial, sans-serif; font-weight: 500; letter-spacing: 1px; white-space: nowrap; }
  .masthead .wordmark { font-size: 68px; color: var(--brand-blue); }

  .showcase { position: absolute; top: 210px; left: 0; width: 1200px; height: 445px;
    background: linear-gradient(180deg, var(--band-top) 0%, var(--band-mid) 55%, var(--band-glow) 88%, #cfe8f8 99%, #ffffff 100%); }
  .floor { position: absolute; top: 655px; left: 0; width: 1200px; height: 245px;
    background: linear-gradient(180deg, var(--floor-top) 0%, var(--floor-bottom) 100%); }

  .card { position: absolute; top: 281px; width: 510px; height: 290px;
    box-shadow: -6px 8px 14px rgba(0, 20, 45, 0.55); overflow: hidden; }
  .card--front { left: 62px; background: var(--brand-navy); }
  .card--back { left: 635px; background: var(--paper); display: flex; align-items: center; justify-content: center; }

  .card__top { position: absolute; inset: 0 0 auto 0; height: 177px; background: var(--brand-blue);
    text-align: center; color: var(--text-light); }
  .card__top .wordmark { display: block; margin-top: 34px; font-size: 41px; }
  .card__name { margin-top: 24px; font-size: 20px; letter-spacing: 1px; }
  .card__role { margin-top: 2px; font-size: 13px; letter-spacing: 1.6px; }
  .card__divider { position: absolute; left: 0; top: 170px; width: 510px; height: 12px; }

  .card__contact { position: absolute; left: 19px; top: 218px; list-style: none;
    color: var(--text-light); font-size: 11.5px; line-height: 15px; letter-spacing: 0.6px; }

  .card--back .wordmark { font-size: 40px; color: var(--brand-blue); }

  .side-label { position: absolute; top: 603px; font-family: "Cormorant Garamond", Georgia, serif;
    font-size: 17px; letter-spacing: 2.5px; color: var(--label); }
  .side-label--front { left: 86px; }
  .side-label--back { left: 658px; }
</style>
</head>
<body>
<main class="board">
  <header class="masthead">
    <span class="wordmark">LOEBER SOLUTIONS</span>
  </header>

  <section class="showcase"></section>
  <section class="floor"></section>

  <article class="card card--front">
    <div class="card__top">
      <span class="wordmark">LOEBER SOLUTIONS</span>
      <p class="card__name">Matthias Loeber</p>
      <p class="card__role">WEB DEVELOPER</p>
    </div>
    <svg class="card__divider" viewBox="0 0 510 12" aria-hidden="true">
      <path d="M0 7 C120 4 380 3 510 6 L510 8 C380 6 120 7 0 9 Z" fill="#ffffff"/>
    </svg>
    <ul class="card__contact">
      <li>Loeber Solutions</li>
      <li>Phone: +41 76 482 17 05</li>
      <li>Web: www.loeber-solutions.example</li>
      <li>Email: matthias@loeber-solutions.example</li>
    </ul>
  </article>

  <article class="card card--back">
    <span class="wordmark">LOEBER SOLUTIONS</span>
  </article>

  <p class="side-label side-label--front">FRONT</p>
  <p class="side-label side-label--back">BACK</p>
</main>
</body>
</html>
```